Innovation Company Business Card Design

I need to have my business card updated. The current card was designed when the company started 2.5 years ago and was a quick and dirty job.

I need a new card design that is more professional and has my updated company tag line.

I will include the old card's Corel Draw file, and EPS versions as examples of the current design. I will also include the company logo eps and corel version files.

The company pantone colour is pantone 1805 c (a dark red)

I want the design to convey the nature of our business as a strategic technology innovation company, but yet still be professional. We are funky vibey and work from an industrial style office in a vibey designer dominat part of town. Though are clients include large banks and corporate clients too.

The information that needs to be on the card is in attached word document (but doesn't have to be in this order or format)

Final version needs to be supplied in PNG preview, as well as PSD file format (or other editable file version) so that personal information on card can be easily edited and reprinted.

Target Market(s)

CEO's of small to medium size companies
Marketing Managers of large coporates
Account managers of Digital Agencies

Industry/Entity Type

Business

Requirements
Must have
• 86x54mm will be cut in rounded corner credit card size format (Except if you recommend otherwise in your design)
Nice to have
• Some kind of background transparency combined with the pantone colour that gives the card some dimension and depth. But no gradient fills please :-)
Should not have
• Basic gradient fills
• Clipart

```html
<!DOCTYPE html>
<html lang="en">
<head>
<meta charset="utf-8">
<title>Fennavo Business Card</title>
<link rel="stylesheet" href="https://fonts.googleapis.com/css2?family=Ubuntu:wght@400;500;700&family=Arimo:wght@400&display=swap">
<style>
  :root {
    --brand-red: #ab1c28;
    --brand-red-deep: #951b25;
    --card-white: #fbfbfa;
    --ink: #2f2f2f;
    --backdrop: #e8e5e1;
    --on-red: #ffffff;
  }
  * { margin: 0; padding: 0; box-sizing: border-box; }
  html, body {
    width: 1200px; height: 900px; overflow: hidden;
    background: var(--backdrop);
    font-family: "Ubuntu", sans-serif;
  }
  .canvas { position: relative; width: 1200px; height: 900px; }

  .card {
    position: absolute; left: 376px; width: 444px; height: 279px;
    overflow: hidden;
    box-shadow: 0 2px 6px rgba(0,0,0,0.18);
  }
  .card-front {
    top: 161px; background: var(--card-white);
    border-radius: 22px 0 22px 0;
  }
  .card-back {
    top: 471px; background: var(--brand-red);
    border-radius: 0 22px 0 22px;
  }

  .wordmark {
    position: absolute; font-family: "Ubuntu", sans-serif;
    font-weight: 700; letter-spacing: 0; line-height: 1;
  }
  .card-front .wordmark {
    left: 28px; top: 28px; font-size: 46px; color: var(--brand-red);
  }
  .card-back .wordmark {
    left: 0; width: 100%; text-align: center; top: 101px;
    font-size: 58px; color: var(--on-red);
  }
  .tagline {
    position: absolute; right: 92px; top: 156px;
    font-family: "Arimo", sans-serif; font-size: 15px; color: var(--on-red);
  }

  .person-name {
    position: absolute; left: 30px; top: 134px;
    font-size: 20px; font-weight: 400; color: var(--ink);
  }
  .person-role {
    position: absolute; left: 30px; top: 159px;
    font-size: 13px; color: var(--brand-red); letter-spacing: 0.3px;
  }

  .contact-list {
    position: absolute; left: 32px; top: 205px;
    list-style: none; font-size: 14px; color: var(--ink);
  }
  .contact-list li { height: 18.5px; line-height: 18.5px; display: flex; }
  .contact-label { width: 26px; color: var(--brand-red); }

  .company-address {
    position: absolute; right: 30px; top: 205px;
    text-align: right; font-style: normal; font-size: 14px;
    color: var(--ink); line-height: 18.5px;
  }
  .company-name { color: var(--brand-red); font-weight: 700; }

  .footer-band { position: absolute; left: 0; bottom: 0; width: 100%; height: 46px; }
  .footer-url {
    position: absolute; left: 0; bottom: 12px; width: 100%;
    text-align: center; font-size: 13px; color: var(--on-red);
  }
</style>
</head>
<body>
<main class="canvas">
  <section class="card card-front" aria-label="Card front">
    <div class="wordmark">Fennavo</div>
    <h1 class="person-name">Daniel Marsh</h1>
    <p class="person-role">FOUNDER &amp; MD</p>
    <ul class="contact-list">
      <li><span class="contact-label">T</span>0815550142</li>
      <li><span class="contact-label">E</span>daniel@fennavo.com</li>
      <li><span class="contact-label">W</span>www.fennavo.com</li>
    </ul>
    <address class="company-address">
      <span class="company-name">Fennavo (Pty) Ltd</span><br>
      Suite 210, 14 Birchwood Ave.<br>
      Parkview, JHB, RSA
    </address>
  </section>

  <section class="card card-back" aria-label="Card back">
    <div class="wordmark">Fennavo</div>
    <p class="tagline">Ideas Built to Last</p>
    <svg class="footer-band" viewBox="0 0 444 46" preserveAspectRatio="none" aria-hidden="true">
      <path d="M0 11 Q222 -9 444 11 L444 46 L0 46 Z" fill="var(--brand-red-deep)"/>
      <path d="M0 11 Q222 -9 444 11" fill="none" stroke="var(--on-red)" stroke-width="3"/>
    </svg>
    <p class="footer-url">www.fennavo.com</p>
  </section>
</main>
</body>
</html>
```